Solvane Vitality MediSpa Brochure

We need a new brochure design. The old is attached.

We are wanting a three panel brochure for med spa designed and ready for print. The brochure will have content and images on both sides. We attached the old brochure in pdf format. The content needs to stay as on the attached pdf but please feel free to offer new designs. The color needs to match the attached logo, which is a light blue and teal. All images we want on the brochure are also attached.

The design must have an 1/8 in space from each edge for printing purposes

Target Market(s)

Men and Women

Industry/Entity Type

Wellness

Font styles to use
Sans Serif

Colors
34a6d7
33b8a4

Requirements
Must have
• soft curves. must have a 1/8 in space on all edges (including interior) to give bleed space for printing. Use content written on attached brochure.

```html
<!DOCTYPE html>
<html lang="en">
<head>
<meta charset="utf-8">
<title>Solvane Vitality MediSpa – Tri-fold Brochure</title>
<link rel="stylesheet" href="https://fonts.googleapis.com/css2?family=Questrial&family=Josefin+Sans:wght@400;600&display=swap">
<style>
  :root{
    --backdrop:#8c8c8c;
    --paper:#dcedf1;
    --paper-light:#eef7f9;
    --teal-deep:#0c6f76;
    --teal-soft:#5b9fa4;
    --teal-title:#3f8c92;
    --ink:#1d2b2e;
    --white:#ffffff;
    --skin-1:#f3e4dc;
    --skin-2:#fbf6f3;
  }
  *{box-sizing:border-box;margin:0;padding:0}
  html,body{width:1200px;height:1000px;overflow:hidden}
  body{background:var(--backdrop);font-family:"Questrial",sans-serif;color:var(--ink);position:relative}
  .sheet{position:absolute;left:30px;top:120px;width:1140px;height:760px;background:var(--paper);overflow:hidden}
  .fold{position:absolute;top:0;bottom:0;width:1px;background:rgba(12,111,118,.15)}
  .fold--one{left:380px}.fold--two{left:760px}

  /* left panel */
  .info-box{position:absolute;left:22px;width:336px;background:var(--teal-soft);color:var(--white);padding:0 0 14px}
  .info-box__title{background:var(--teal-title);font-family:"Josefin Sans",sans-serif;font-weight:600;font-size:17px;letter-spacing:.5px;padding:8px 14px 5px;text-transform:uppercase}
  .info-box p{font-size:13.5px;line-height:1.35;padding:8px 14px 0}
  .info-box ul{list-style:none;padding:8px 14px 0;font-size:14px;line-height:1.35}
  .info-box--premier{top:40px}
  .info-box--why{top:190px}
  .info-box--members{top:368px}
  .learn-more{position:absolute;left:22px;top:610px;width:336px;height:100px;background:var(--teal-deep);color:var(--white);text-align:center;padding:28px 12px 0}
  .learn-more__label{font-size:15px}
  .learn-more__url{font-size:14px;margin-top:6px;overflow-wrap:anywhere}

  /* middle panel */
  .quote-box{position:absolute;left:402px;top:36px;width:336px;height:392px;background:var(--teal-deep);color:var(--white);padding:24px 22px}
  .quote-box p{font-size:14.5px;line-height:1.38;margin-bottom:14px}
  .quote-box__sign{font-family:"Josefin Sans",sans-serif;font-size:16px;letter-spacing:.6px;margin-top:20px}
  .contact{position:absolute;left:412px;top:460px;width:330px}
  .contact h3{font-family:"Josefin Sans",sans-serif;font-weight:400;font-size:19px;letter-spacing:.4px;margin-bottom:3px}
  .contact p{font-size:12.5px;line-height:1.35}
  .contact .gap{height:18px}
  .contact .lines p{font-size:14px}

  /* right panel */
  .tagline-tab{position:absolute;left:850px;top:0;width:260px;height:28px;background:var(--teal-deep);color:var(--white);font-family:"Josefin Sans",sans-serif;font-weight:600;font-size:13px;letter-spacing:1px;text-align:center;padding-top:8px}
  .brand{position:absolute;left:880px;top:42px;display:flex;align-items:center;gap:10px}
  .brand__dot{width:14px;height:14px;border-radius:50%;background:var(--teal-deep)}
  .brand__name{font-size:17px;color:var(--teal-deep)}
  .portrait{position:absolute;left:760px;top:92px;width:380px;height:300px;background:linear-gradient(135deg,var(--skin-2),var(--skin-1) 60%,var(--skin-2))}
  .curves{position:absolute;left:380px;top:0;width:760px;height:760px;pointer-events:none}
  .services{position:absolute;left:898px;top:470px;width:220px;height:190px;background:var(--teal-deep);color:var(--white);padding:14px 16px}
  .services h3{font-family:"Josefin Sans",sans-serif;font-weight:600;font-size:14px;letter-spacing:.6px;margin-bottom:8px;white-space:nowrap}
  .services ul{list-style:none;font-size:14px;line-height:1.45}
</style>
</head>
<body>
<main class="sheet">
  <div class="fold fold--one"></div>
  <div class="fold fold--two"></div>

  <section class="info-box info-box--premier">
    <h2 class="info-box__title">Fernridge's Premier MediSpa</h2>
    <p>Solvane Vitality MediSpa is the premier medical spa in Fernridge, TX. We utilize the best equipment available today for laser treatments, dermal fillers, facials, injections, chemical peels and wellness solutions.</p>
  </section>

  <section class="info-box info-box--why">
    <h2 class="info-box__title">Why Choose Our MediSpa?</h2>
    <p>Under the supervision of Dr. Elena Hartwell, our medical staff provides state-of-the-art cosmetic treatments to both women and men.</p>
    <p>Our staff is trained to provide unique medical spa services to help our clients achieve a more youthful look and defy the aging process.</p>
  </section>

  <section class="info-box info-box--members">
    <h2 class="info-box__title">Exclusive Memberships</h2>
    <p>Our exclusive membership packages are tailored for our clients and created to give them an exceptional experience at a discounted price.</p>
    <ul>
      <li>• SILVER Membership</li>
      <li>• GOLD Membership</li>
      <li>• PLATINUM Membership</li>
    </ul>
  </section>

  <div class="learn-more">
    <div class="learn-more__label">Learn More At</div>
    <div class="learn-more__url">www.SolvaneVitalityMedispa.com/memberships</div>
  </div>

  <section class="quote-box">
    <p>“Rejuvenation and reconstruction of the face are my passion, whether it is to improve one's visual functions or to enhance one's appearance.”</p>
    <p>“I personally perform all of my injections and CO<sub>2</sub> laser treatments because safety and satisfaction are my top priorities.”</p>
    <p>“I was called by God to become a physician at the age of seven years old. I am motivated by a desire to serve others by providing superb medical care. I constantly strive to do my best.”</p>
    <div class="quote-box__sign">DR. ELENA HARTWELL, MD FACS</div>
  </section>

  <section class="contact">
    <h3>LOCATION</h3>
    <p>2480 Meadowline Dr<br>Suite 140<br>Fernridge TX 75010</p>
    <div class="gap"></div>
    <h3>SCHEDULE A CONSULTATION</h3>
    <div class="lines">
      <p>Ph: (555) 214-3016</p>
      <p>Fax: (555) 214-6565</p>
    </div>
    <div class="gap"></div>
    <div class="lines">
      <p>glow@elenahartwellmd.com</p>
      <p>www.SolvaneVitalityMedispa.com</p>
    </div>
  </section>

  <div class="tagline-tab">REFRESH AND REJUVENATE</div>
  <div class="brand"><span class="brand__dot"></span><span class="brand__name">Solvane Vitality MediSpa</span></div>

  <div class="portrait" role="img" aria-label="Close-up portrait photograph of a woman with smooth, glowing skin"></div>

  <svg class="curves" viewBox="0 0 760 760" aria-hidden="true">
    <path d="M380 392 Q 560 330 760 300 L760 320 Q 560 350 380 410 Z" fill="var(--paper)"/>
    <path d="M380 400 Q 560 345 760 312" fill="none" stroke="var(--teal-deep)" stroke-width="2"/>
    <path d="M0 20 Q 190 10 380 0" fill="none" stroke="var(--teal-deep)" stroke-width="2"/>
  </svg>

  <section class="services">
    <h3>FOR WOMEN AND MEN</h3>
    <ul>
      <li>• Laser Treatments</li>
      <li>• Dermal Fillers</li>
      <li>• Neurotoxins</li>
      <li>• Facials</li>
      <li>• Chemical Peels</li>
      <li>• Wellness Treatments</li>
    </ul>
  </section>
</main>
</body>
</html>
```